Design mobile friendly real estate and property management company landing page

Design a clean, crisp modern looking landing page that is mobile-friendly (must resize, preferably using bootstrap framework). Landing page will consist of heading with login area, company info, body consists of company description and services, a list of available rental properties with photos, and a footer with additional links and info. Working on updating with text for text areas marked A, B, and C on the layout pdf, but in meantime, lorem ipsum is fine. I can connect events to most buttons, etc. Just need the bootstrap and html functionality set up. Previous company website (which should not be relied upon) is www.qlbt.net This is somewhat of a template for a start, but looking for a more professional and modern design for the new website. But this gives an idea of the content and what needs to be displayed, and how.

Target Market(s)

Clients looking for a property management company that is efficient and well-organized.

Industry/Entity Type

Property Management

Coding

Coded - Design and coding required

Number of Pages Required

1 page

Font styles to use
Sans Serif

Colors
0355a3

Requirements
Must have
• Resize for the screen using bootstrap.
• Navigation that collapses for mobile devices
• Large text boxes and good solid spacing around all elements.
Nice to have
• for property images it would be nice if they can be swiped on touch enabled devices (to the next or previous image). And have navigation that can be clicked to next or previous images.
• Would be nice if a captcha verification was included on contact form.
Should not have
• Fancy or eccentric art

```html
<!DOCTYPE html>
<html lang="en">
<head>
<meta charset="utf-8">
<title>Northgate Realty Services</title>
<link href="https://fonts.googleapis.com/css2?family=Open+Sans:wght@400;600;700;800&display=swap" rel="stylesheet">
<style>
:root{
  --navy:#0c1b33;
  --navy-2:#14284a;
  --blue:#0355a3;
  --ink:#222;
  --muted:#666;
  --line:#dcdcdc;
  --grey-bg:#ececec;
  --cell:#f1f1f1;
  --white:#fff;
}
*{box-sizing:border-box;margin:0;padding:0}
html,body{width:1200px;height:2228px;overflow:hidden}
body{font-family:"Open Sans",Arial,sans-serif;color:var(--ink);background:var(--white);position:relative}
.topbar{height:76px;background:var(--navy);display:flex;align-items:center;justify-content:space-between;padding:0 64px}
.brand{color:var(--white);line-height:1}
.brand-name{font-size:22px;font-weight:700;letter-spacing:1px;display:block}
.brand-sub{font-size:11px;letter-spacing:4px;font-weight:400;display:block;text-align:center;margin-top:4px}
.contact-bar{display:flex;align-items:center;gap:16px;color:var(--white)}
.call{display:flex;align-items:center;gap:10px}
.call small{display:block;font-size:11px;opacity:.8}
.call strong{font-size:18px;font-weight:600}
.login{background:var(--white);color:var(--navy);font-size:12px;font-weight:700;padding:9px 22px;border-radius:2px}
.mainnav{height:32px;display:flex;justify-content:center;gap:0;border-bottom:1px solid var(--line)}
.mainnav a{font-size:11px;font-weight:600;color:var(--ink);text-decoration:none;line-height:32px;padding:0 52px}
.hero{position:relative;height:660px;background:linear-gradient(180deg,#5e8a95 0%,#7fa9ae 35%,#3d5a66 65%,#14202b 100%)}
.hero-photo{position:absolute;inset:0}
.hero-text{position:absolute;left:64px;top:176px;width:520px;color:var(--navy)}
.hero-text h2{font-size:30px;font-weight:400}
.hero-text h1{font-size:34px;font-weight:800;margin-top:2px}
.hero-text p{font-size:15px;line-height:1.6;margin-top:22px;color:#12223b}
.btn{display:inline-flex;align-items:center;gap:10px;background:var(--blue);color:var(--white);font-size:12px;font-weight:700;padding:11px 22px;border-radius:2px}
.hero .btn{margin-top:28px}
.contact-box{position:absolute;left:772px;top:100px;width:328px;height:440px;background:rgba(12,27,51,.85);padding:0 20px}
.contact-box h3{color:var(--white);text-align:center;font-size:18px;font-weight:600;padding:14px 0 12px;border-bottom:1px solid rgba(255,255,255,.3);margin:0 -20px 16px}
.field{background:var(--white);height:34px;margin-bottom:12px;font-size:12px;color:#777;padding:9px 10px}
.field.area{height:80px}
.send{background:var(--blue);color:var(--white);text-align:center;font-weight:700;font-size:13px;padding:12px 0;margin-top:6px}
.services{height:644px;display:flex;border-bottom:1px solid var(--line)}
.service{flex:1;padding:84px 64px 0}
.service+.service{border-left:1px solid var(--line)}
.service h3{display:flex;align-items:center;gap:16px;font-size:26px;font-weight:400;color:var(--navy)}
.service p{font-size:15px;line-height:1.6;color:var(--muted);margin-top:22px}
.service ul{list-style:none;margin-top:30px}
.service li{display:flex;align-items:center;justify-content:space-between;border-bottom:1px solid var(--line);padding:13px 0;font-size:15px;font-weight:600}
.service li span{display:flex;align-items:center;gap:16px}
.dot{width:12px;height:12px;border-radius:50%;background:var(--navy)}
.service .btn{margin-top:48px}
.listings{background:var(--grey-bg);height:704px;padding:100px 64px 0}
.listings h2{font-size:28px;font-weight:600;color:var(--navy);margin-bottom:24px}
.card{background:var(--white);display:flex;height:232px;padding:18px 20px;margin-bottom:40px;gap:28px}
.card-photo{width:260px}
.card-photo h4{color:var(--blue);font-size:22px;font-weight:600;margin-bottom:12px}
.photo{height:150px}
.card-main{flex:1}
.card-main h5{display:flex;align-items:center;gap:10px;font-size:15px;font-weight:700;margin-bottom:16px}
.specs{display:grid;grid-template-columns:1fr 1fr;background:var(--cell);padding:10px 14px;gap:8px 20px;font-size:12px}
.specs div{display:flex;border-bottom:1px solid #e0e0e0;padding-bottom:6px}
.specs b{width:90px;font-weight:600}
.card-side{width:260px}
.card-side h5{font-size:18px;font-weight:600;color:var(--navy);margin-bottom:10px}
.feat{display:flex;align-items:center;gap:10px;font-size:12px;color:var(--blue);font-weight:600;margin-bottom:6px}
.card-side p{font-size:12px;line-height:1.6;color:var(--muted);margin-top:10px}
.footer{position:absolute;left:0;top:2108px;width:1200px;height:120px;background:var(--navy);display:flex;align-items:center;justify-content:space-between;padding:0 64px;color:var(--white);font-size:12px}
.badges{display:flex;gap:14px}
.badge{width:52px;height:52px;background:#dfe4ea}
.foot-links{display:flex;gap:40px;align-items:center}
</style>
</head>
<body>
<header class="topbar">
  <div class="brand"><span class="brand-name">NORTHGATE REALTY</span><span class="brand-sub">SERVICES</span></div>
  <div class="contact-bar">
    <div class="call">
      <svg width="26" height="26" viewBox="0 0 24 24"><path fill="#fff" d="M6.6 10.8a15 15 0 0 0 6.6 6.6l2.2-2.2a1 1 0 0 1 1-.25 11.4 11.4 0 0 0 3.6.6 1 1 0 0 1 1 1V20a1 1 0 0 1-1 1A17 17 0 0 1 3 4a1 1 0 0 1 1-1h3.5a1 1 0 0 1 1 1c0 1.25.2 2.45.6 3.6a1 1 0 0 1-.25 1z"/></svg>
      <div><small>Call us</small><strong>123 456 7890</strong></div>
    </div>
    <span class="login">LOGIN</span>
  </div>
</header>
<nav class="mainnav">
  <a href="#">HOME</a><a href="#">FOR RENT</a><a href="#">FOR SALE</a><a href="#">PROPERTY MANAGEMENT</a><a href="#">REAL ESTATE</a><a href="#">ABOUT</a>
</nav>
<section class="hero">
  <div class="hero-photo" role="img" aria-label="City skyline with palm trees at dusk"></div>
  <div class="hero-text">
    <h2>Welcome to</h2>
    <h1>NORTHGATE REALTY SERVICES</h1>
    <p>Lorem ipsum dolor sit amet, consectetuer adipiscing elit, sed diam nonummy nibh euismod tincidunt ut laoreet dolore magna aliquam erat volutpat. Ut wisi enim ad minim veniam, quis nostrud exerci tation ullamcorper suscipit lobortis nisl ut aliquip.</p>
    <span class="btn">LEARN MORE <svg width="14" height="10" viewBox="0 0 14 10"><path d="M0 5h12M8 1l4 4-4 4" stroke="#fff" stroke-width="1.6" fill="none"/></svg></span>
  </div>
  <form class="contact-box">
    <h3>CONTACT US</h3>
    <div class="field">Name</div>
    <div class="field">Email</div>
    <div class="field">Phone</div>
    <div class="field">Subject</div>
    <div class="field area">Comments</div>
    <div class="send">SEND</div>
  </form>
</section>
<section class="services">
  <div class="service">
    <h3><svg width="32" height="28" viewBox="0 0 32 28"><rect x="2" y="14" width="6" height="12" fill="#0355a3"/><rect x="12" y="8" width="6" height="18" fill="#0355a3"/><rect x="22" y="2" width="6" height="24" fill="#0355a3"/></svg>Property Management Services</h3>
    <p>Lorem ipsum dolor sit amet, consectetuer adipiscing elit, sed diam nonummy nibh euismod tincidunt ut laoreet dolore magna aliquam erat volutpat. Ut wisi enim ad minim veniam, quis nostrud exerci tation ullamcorper suscipit lobortis nisl ut aliquip ex ea commodo consequat.</p>
    <ul>
      <li><span><i class="dot"></i>Properties Management</span><svg width="16" height="12" viewBox="0 0 16 12"><path d="M0 6h14M9 1l5 5-5 5" stroke="#222" stroke-width="1.5" fill="none"/></svg></li>
      <li><span><i class="dot"></i>Property Analysis</span><svg width="16" height="12" viewBox="0 0 16 12"><path d="M0 6h14M9 1l5 5-5 5" stroke="#222" stroke-width="1.5" fill="none"/></svg></li>
      <li><span><i class="dot"></i>Marketing and Leasing</span><svg width="16" height="12" viewBox="0 0 16 12"><path d="M0 6h14M9 1l5 5-5 5" stroke="#222" stroke-width="1.5" fill="none"/></svg></li>
    </ul>
    <span class="btn">VIEW MORE</span>
  </div>
  <div class="service">
    <h3><svg width="32" height="28" viewBox="0 0 32 28"><path d="M16 2 2 14h4v12h20V14h4z" fill="#0355a3"/></svg>Real Estate Services</h3>
    <p>Lorem ipsum dolor sit amet, consectetuer adipiscing elit, sed diam nonummy nibh euismod tincidunt ut laoreet dolore magna aliquam erat volutpat. Ut wisi enim ad minim veniam, quis nostrud exerci tation ullamcorper suscipit lobortis nisl ut aliquip ex ea commodo consequat.</p>
    <ul>
      <li><span><i class="dot"></i>Real Estate Consulting</span><svg width="16" height="12" viewBox="0 0 16 12"><path d="M0 6h14M9 1l5 5-5 5" stroke="#222" stroke-width="1.5" fill="none"/></svg></li>
      <li><span><i class="dot"></i>Sales</span><svg width="16" height="12" viewBox="0 0 16 12"><path d="M0 6h14M9 1l5 5-5 5" stroke="#222" stroke-width="1.5" fill="none"/></svg></li>
      <li><span><i class="dot"></i>Estate Management</span><svg width="16" height="12" viewBox="0 0 16 12"><path d="M0 6h14M9 1l5 5-5 5" stroke="#222" stroke-width="1.5" fill="none"/></svg></li>
    </ul>
    <span class="btn">VIEW MORE</span>
  </div>
</section>
<section class="listings">
  <h2>FEATURED LISTINGS</h2>
  <article class="card">
    <div class="card-photo"><h4>For Rent</h4><div class="photo" role="img" aria-label="Modern living room interior" style="background:linear-gradient(135deg,#d9d6cf,#8e8a82)"></div></div>
    <div class="card-main">
      <h5><svg width="14" height="18" viewBox="0 0 14 18"><path d="M7 0a7 7 0 0 0-7 7c0 5 7 11 7 11s7-6 7-11a7 7 0 0 0-7-7zm0 10a3 3 0 1 1 0-6 3 3 0 0 1 0 6z" fill="#0c1b33"/></svg>Lorem ipsum dolor sit amet, consectetuer adipiscing elit</h5>
      <div class="specs">
        <div><b>Rent :</b>$1,000.00</div><div><b>Community :</b>North Fork</div>
        <div><b>Available :</b>3/11/2016</div><div><b>Parking :</b>2 assigned spaces</div>
        <div><b>Sqft :</b>870</div><div><b>Pets :</b>Allowed</div>
        <div><b>Lease :</b>12 Months</div><div><b>Laundry :</b>On Site</div>
      </div>
    </div>
    <div class="card-side">
      <h5>Suscipit Lobortis</h5>
      <div class="feat"><svg width="20" height="12" viewBox="0 0 20 12"><rect y="4" width="20" height="6" fill="#0355a3"/><rect y="0" width="8" height="5" fill="#0355a3"/></svg>2 Bedroom</div>
      <div class="feat"><svg width="20" height="12" viewBox="0 0 20 12"><path d="M0 4h20v3a5 5 0 0 1-5 5H5a5 5 0 0 1-5-5z" fill="#0355a3"/></svg>1 Bath Condo</div>
      <p>Lorem ipsum dolor sit amet, consectetuer adipiscing elit, sed diam nonummy nibh euismod tincidunt ut laoreet dolore magna aliquam erat.</p>
    </div>
  </article>
  <article class="card">
    <div class="card-photo"><h4>For Sale</h4><div class="photo" role="img" aria-label="Modern house with pool at dusk" style="background:linear-gradient(180deg,#8fb4d6,#4d6f8c 60%,#2f6f9a)"></div></div>
    <div class="card-main">
      <h5><svg width="14" height="18" viewBox="0 0 14 18"><path d="M7 0a7 7 0 0 0-7 7c0 5 7 11 7 11s7-6 7-11a7 7 0 0 0-7-7zm0 10a3 3 0 1 1 0-6 3 3 0 0 1 0 6z" fill="#0c1b33"/></svg>Lorem ipsum dolor sit amet, consectetuer adipiscing elit</h5>
      <div class="specs">
        <div><b>Rent :</b>$1,000.00</div><div><b>Community :</b>North Fork</div>
        <div><b>Available :</b>3/11/2016</div><div><b>Parking :</b>2 assigned spaces</div>
        <div><b>Sqft :</b>870</div><div><b>Pets :</b>Allowed</div>
        <div><b>Lease :</b>12 Months</div><div><b>Laundry :</b>On Site</div>
      </div>
    </div>
    <div class="card-side">
      <h5>Suscipit Lobortis</h5>
      <div class="feat"><svg width="20" height="12" viewBox="0 0 20 12"><rect y="4" width="20" height="6" fill="#0355a3"/><rect y="0" width="8" height="5" fill="#0355a3"/></svg>2 Bedroom</div>
      <div class="feat"><svg width="20" height="12" viewBox="0 0 20 12"><path d="M0 4h20v3a5 5 0 0 1-5 5H5a5 5 0 0 1-5-5z" fill="#0355a3"/></svg>1 Bath Condo</div>
      <p>Lorem ipsum dolor sit amet, consectetuer adipiscing elit, sed diam nonummy nibh euismod tincidunt ut laoreet dolore magna aliquam erat.</p>
    </div>
  </article>
</section>
<footer class="footer">
  <div class="badges"><span class="badge"></span><span class="badge"></span><span class="badge"></span></div>
  <div class="foot-links"><span>Privacy and Policy</span><span>© 2016 Northgate Realty Services</span></div>
</footer>
</body>
</html>
```